Conference banner for Beacon training organisation

We empower everyday heroes.
We provide training that empowers individuals to create positive change in themselves, their community, and the world.
We need a large banner design to promote the organisation at conferences and events. We are open to ideas and creativity.
It may involve creatively displaying our logo only, or it may involve our logo and a summary of our products (Beacon training, Steady Minds Crisis Care).
Size: 820mm width x 1790mm height
300dpi
Target Market(s)
Educators and frontline health, community, and social workers.
Industry/Entity Type
Training
Colors
Designer to choose colors to be used in the design.

```html
<!DOCTYPE html>
<html lang="en">
<head>
<meta charset="utf-8">
<title>Beacon Training – Conference Banner Options</title>
<link href="https://fonts.googleapis.com/css2?family=Fira+Sans+Condensed:ital,wght@0,600;1,500&family=Open+Sans:wght@700&display=swap" rel="stylesheet">
<style>
  :root {
    --label-bar: #fff200;
    --ink: #111111;
    --rose: #c4475a;
    --rose-light: #cf5a6c;
    --rose-soft: #d46a7a;
    --wine: #9c2f40;
    --wine-text: #a02e3f;
    --blush: #f6c9cf;
    --brand-blue: #2a5db0;
    --dot-blue: #2f66b3;
    --slate: #555555;
    --paper: #ffffff;
  }
  * { box-sizing: border-box; margin: 0; padding: 0; }
  html, body { width: 1200px; height: 878px; overflow: hidden; }
  body {
    position: relative;
    font-family: "Fira Sans Condensed", "Arial Narrow", sans-serif;
    background: linear-gradient(100deg, #ffffff 0%, #e6e6e6 22%, #8a8a8a 45%, #2a2a2a 62%, #000000 75%);
  }
  .board-shade {
    position: absolute; left: 0; top: 83px; width: 420px; height: 795px;
    background: linear-gradient(180deg, rgba(0,0,0,0) 20%, rgba(0,0,0,0.75) 100%);
  }
  .option-bar {
    position: absolute; left: 0; top: 0; width: 1200px; height: 83px;
    background: var(--label-bar);
  }
  .option-label {
    position: absolute; top: 27px; width: 240px; text-align: center;
    font-family: "Open Sans", Arial, sans-serif; font-weight: 700;
    font-size: 30px; line-height: 40px; color: var(--ink); letter-spacing: 0.5px;
  }
  .banner { position: absolute; width: 343px; overflow: hidden; }
  .banner svg.art { position: absolute; left: 0; top: 0; width: 100%; height: 100%; }
  .banner .abs { position: absolute; }

  .title-main { font-weight: 600; font-size: 36px; line-height: 42px; text-transform: uppercase; white-space: nowrap; }
  .title-sub { font-weight: 600; font-size: 32px; line-height: 36px; text-transform: uppercase; white-space: nowrap; }

  .certify { display: flex; align-items: center; gap: 10px; }
  .certify svg { width: 40px; height: 50px; flex: none; }
  .certify-text { font-style: italic; font-weight: 500; font-size: 19px; line-height: 22px; white-space: nowrap; }

  .brand { display: flex; align-items: center; gap: 10px; font-weight: 600; font-size: 36px; line-height: 40px; color: var(--brand-blue); letter-spacing: 1px; }
  .brand-dot { width: 20px; height: 20px; border-radius: 50%; background: var(--rose); flex: none; }

  .banner--one { left: 51px; top: 106px; height: 749px; background: var(--rose); }
  .banner--two { left: 424px; top: 106px; height: 749px; background: var(--paper); }
  .banner--three { left: 802px; top: 110px; height: 748px; background: var(--paper); }
</style>
</head>
<body>
  <div class="board-shade"></div>
  <header class="option-bar">
    <div class="option-label" style="left:115px">OPTION -1</div>
    <div class="option-label" style="left:480px">OPTION -2</div>
    <div class="option-label" style="left:860px">OPTION -3</div>
  </header>

  <!-- Option 1 -->
  <section class="banner banner--one">
    <svg class="art" viewBox="0 0 343 749" preserveAspectRatio="none">
      <defs>
        <linearGradient id="skyline-one" x1="0" y1="0" x2="0" y2="1">
          <stop offset="0" stop-color="#cf5a6c" stop-opacity="0"/>
          <stop offset="1" stop-color="#cf5a6c" stop-opacity="0.8"/>
        </linearGradient>
      </defs>
      <rect x="0" y="350" width="343" height="300" fill="url(#skyline-one)" role="img" aria-label="Faint city skyline silhouette"/>
      <path d="M0 640 Q60 625 130 610 Q150 555 215 555 Q280 555 300 610 Q325 610 343 600 L343 749 L0 749 Z" fill="var(--paper)"/>
    </svg>
    <div class="abs certify" style="left:24px;top:30px">
      <svg viewBox="0 0 40 50"><path d="M10 30 L6 48 L14 43 L18 49 L20 34 Z M30 30 L34 48 L26 43 L22 49 L20 34 Z" fill="var(--blush)"/><circle cx="20" cy="20" r="17" fill="var(--blush)"/><path d="M12 20 L18 26 L28 14" fill="none" stroke="var(--rose)" stroke-width="3.5" stroke-linecap="round" stroke-linejoin="round"/></svg>
      <div class="certify-text" style="color:var(--blush)">Get Certified<br>FIRST AID TRAINING!</div>
    </div>
    <div class="abs" style="left:37px;top:172px;color:var(--paper)">
      <div class="title-main">Beacon Training</div>
      <div class="title-sub">Steady Minds<br>Crisis Care</div>
    </div>
    <div class="abs brand" style="left:64px;top:687px"><span class="brand-dot"></span>LANTERNFIELD</div>
  </section>

  <!-- Option 2 -->
  <section class="banner banner--two">
    <svg class="art" viewBox="0 0 343 749" preserveAspectRatio="none">
      <defs>
        <linearGradient id="skyline-two" x1="0" y1="0" x2="0" y2="1">
          <stop offset="0" stop-color="#d46a7a" stop-opacity="0"/>
          <stop offset="1" stop-color="#d46a7a" stop-opacity="0.75"/>
        </linearGradient>
      </defs>
      <path d="M0 240 Q120 200 200 195 Q290 192 343 230 L343 749 L0 749 Z" fill="var(--rose)"/>
      <path d="M0 305 Q110 290 190 262 Q280 232 343 270 L343 749 L0 749 Z" fill="var(--wine)"/>
      <rect x="0" y="470" width="343" height="279" fill="url(#skyline-two)" role="img" aria-label="City skyline silhouette"/>
    </svg>
    <div class="abs brand" style="left:53px;top:128px"><span class="brand-dot"></span>LANTERNFIELD</div>
    <div class="abs" style="left:40px;top:345px;color:var(--paper)">
      <div class="title-main">Beacon Training</div>
      <div class="title-sub" style="font-size:29px;line-height:33px">Steady Minds<br>Crisis Care</div>
    </div>
    <div class="abs certify" style="left:42px;top:502px">
      <svg viewBox="0 0 40 50"><path d="M10 30 L6 48 L14 43 L18 49 L20 34 Z M30 30 L34 48 L26 43 L22 49 L20 34 Z" fill="var(--blush)"/><circle cx="20" cy="20" r="17" fill="var(--blush)"/><path d="M12 20 L18 26 L28 14" fill="none" stroke="var(--wine)" stroke-width="3.5" stroke-linecap="round" stroke-linejoin="round"/></svg>
      <div class="certify-text" style="color:var(--blush)">Get Certified<br>FIRST AID TRAINING!</div>
    </div>
  </section>

  <!-- Option 3 -->
  <section class="banner banner--three">
    <svg class="art" viewBox="0 0 343 748" preserveAspectRatio="none">
      <defs>
        <linearGradient id="skyline-three" x1="0" y1="0" x2="0" y2="1">
          <stop offset="0" stop-color="#c4475a" stop-opacity="0"/>
          <stop offset="0.5" stop-color="#c4475a" stop-opacity="0.55"/>
          <stop offset="1" stop-color="#c4475a" stop-opacity="1"/>
        </linearGradient>
      </defs>
      <rect x="0" y="187" width="343" height="59" fill="var(--rose)"/>
      <rect x="100" y="440" width="243" height="290" fill="url(#skyline-three)" role="img" aria-label="City skyline illustration"/>
      <path d="M0 720 Q120 690 260 695 Q320 700 343 720 L343 748 L0 748 Z" fill="var(--rose)"/>
      <circle cx="288" cy="680" r="46" fill="var(--dot-blue)"/>
    </svg>
    <div class="abs brand" style="left:50px;top:125px"><span class="brand-dot"></span>LANTERNFIELD</div>
    <div class="abs" style="left:28px;top:196px">
      <div class="title-main" style="color:var(--paper);font-size:38px">Beacon Training</div>
      <div class="title-sub" style="color:var(--wine-text);font-size:30px;line-height:34px;margin-top:12px">Steady Minds<br>Crisis Care</div>
    </div>
    <div class="abs certify" style="left:46px;top:360px">
      <svg viewBox="0 0 40 50"><path d="M10 30 L6 48 L14 43 L18 49 L20 34 Z M30 30 L34 48 L26 43 L22 49 L20 34 Z" fill="var(--slate)"/><circle cx="20" cy="20" r="17" fill="var(--slate)"/><path d="M12 20 L18 26 L28 14" fill="none" stroke="var(--paper)" stroke-width="3.5" stroke-linecap="round" stroke-linejoin="round"/></svg>
      <div class="certify-text" style="color:var(--slate)">Get Certified<br>FIRST AID TRAINING!</div>
    </div>
  </section>
</body>
</html>
```